Newsletter template

I am looking for 2 newsletter templates. My website is in Wordpress and I want to use in mailchimp for lists.

One newsletter is for local clients of design remodeling firm to be sent monthly

Second newsletter is for web store offerings to be sent weekly.

Target Market(s)

Luxury home and leisure

Industry/Entity Type

Store

Requirements
Must have
• Use logos and colors to seamlessly integrate with website,

```html
<!DOCTYPE html>
<html lang="en">
<head>
<meta charset="utf-8">
<title>Elsie Marlowe Fine Living — Newsletter Template</title>
<link rel="stylesheet" href="https://fonts.googleapis.com/css2?family=Source+Sans+3:wght@400;600&display=swap">
<style>
  :root {
    --teal: #00a9c6;
    --teal-soft: #5cc8d9;
    --lime: #d4dc1f;
    --panel: #f2f2f3;
    --ink: #1b1b1b;
    --muted: #9a9a9a;
    --white: #ffffff;
  }
  * { margin: 0; padding: 0; box-sizing: border-box; }
  html, body { width: 720px; height: 1200px; overflow: hidden; background: var(--white); }
  body { font-family: "Source Sans 3", "Myriad Pro", Arial, sans-serif; color: var(--ink); }

  .newsletter { position: relative; width: 720px; height: 1200px; background: var(--white); }

  /* Header */
  .top-band { position: absolute; left: 0; top: 0; width: 720px; height: 242px; background: var(--teal); }
  .masthead {
    position: absolute; left: 52px; top: 33px; width: 622px; height: 225px;
    background: linear-gradient(180deg, var(--teal-soft), var(--teal));
  }
  .masthead-panel {
    position: absolute; left: 20px; top: 15px; width: 578px; height: 194px;
    background: var(--panel);
  }
  .brand-name {
    position: absolute; left: 18px; top: 92px;
    font-size: 42px; font-weight: 600; color: var(--teal); letter-spacing: 0.5px; line-height: 1;
  }
  .brand-tagline {
    position: absolute; left: 18px; top: 140px;
    font-size: 20px; font-weight: 400; color: var(--ink); line-height: 1;
  }

  .main-nav {
    position: absolute; left: 52px; top: 258px; width: 622px; height: 36px;
    background: var(--white); border: 1px solid var(--teal);
  }
  .nav-item {
    position: absolute; top: 50%; transform: translate(-50%, -50%);
    font-size: 18px; font-weight: 400; letter-spacing: 0.3px; line-height: 1; white-space: nowrap;
  }
  .nav-sep { font-weight: 600; font-size: 22px; }
  .sep-teal { color: var(--teal); }
  .sep-ink { color: var(--ink); }
  .sep-lime { color: var(--lime); }

  /* Section guides */
  .section-guide {
    position: absolute; left: 360px; transform: translateX(-50%);
    display: flex; flex-direction: column; align-items: center;
    color: var(--muted); font-size: 22px; letter-spacing: 0.3px;
  }
  .guide-header { top: 530px; }
  .guide-footer { top: 700px; }
  .guide-header .guide-label { margin-top: 10px; }
  .guide-footer .guide-label { margin-bottom: 10px; }

  /* Footer */
  .footer-band {
    position: absolute; left: 0; top: 1006px; width: 720px; height: 46px;
    background: linear-gradient(180deg, var(--teal-soft), var(--teal));
    border-top: 1px dashed var(--teal); border-bottom: 1px dashed var(--teal);
  }
  .footer-col { position: absolute; top: 1074px; font-size: 13px; line-height: 18px; }
  .footer-col .marker {
    position: absolute; left: -22px; top: -2px;
    font-size: 20px; font-weight: 600; line-height: 20px;
  }
  .footer-col .col-title { text-transform: uppercase; }
  .footer-col .col-line { padding-left: 0; }
  .col-office { left: 74px; }
  .col-office .col-line { padding-left: 0; }
  .col-mail { left: 265px; }
  .col-contact { left: 474px; }
  .contact-block + .contact-block { margin-top: 18px; position: relative; }
  .contact-block { position: relative; }
  .footer-brand {
    position: absolute; left: 18px; top: 1148px;
    font-size: 42px; font-weight: 600; color: var(--teal); letter-spacing: 0.5px; line-height: 1;
  }
</style>
</head>
<body>
<main class="newsletter">

  <header class="site-header">
    <div class="top-band"></div>
    <div class="masthead" role="img" aria-label="Teal wave pattern border framing the masthead">
      <div class="masthead-panel">
        <div class="brand-name">Elsie Marlowe</div>
        <div class="brand-tagline">FINE LIVING</div>
      </div>
    </div>
    <nav class="main-nav">
      <span class="nav-item" style="left:104px">STYLE</span>
      <span class="nav-item nav-sep sep-teal" style="left:171px">+</span>
      <span class="nav-item" style="left:241px">SHOP</span>
      <span class="nav-item nav-sep sep-ink" style="left:310px">+</span>
      <span class="nav-item" style="left:379px">DESIGN</span>
      <span class="nav-item nav-sep sep-lime" style="left:448px">+</span>
      <span class="nav-item" style="left:517px">HOME</span>
    </nav>
  </header>

  <div class="section-guide guide-header">
    <svg width="28" height="44" viewBox="0 0 28 44" aria-hidden="true">
      <polygon points="14,0 28,20 0,20" fill="#9a9a9a"/>
      <rect x="12" y="18" width="4" height="26" fill="#9a9a9a"/>
    </svg>
    <span class="guide-label">HEADER</span>
  </div>

  <div class="section-guide guide-footer">
    <span class="guide-label">FOOTER</span>
    <svg width="28" height="44" viewBox="0 0 28 44" aria-hidden="true">
      <rect x="12" y="0" width="4" height="26" fill="#9a9a9a"/>
      <polygon points="0,24 28,24 14,44" fill="#9a9a9a"/>
    </svg>
  </div>

  <footer class="site-footer">
    <div class="footer-band" role="img" aria-label="Teal wave pattern band"></div>

    <div class="footer-col col-office">
      <span class="marker sep-teal">+</span>
      <div class="col-title">Our office location</div>
      <div class="col-line">Design studio</div>
      <div class="col-line">412 Harbor Lane S</div>
      <div class="col-line">Seabrook, FL 34190</div>
    </div>

    <div class="footer-col col-mail">
      <span class="marker sep-ink">+</span>
      <div class="col-title">Mailing address</div>
      <div class="col-line">2275 Palm Crest Avenue</div>
      <div class="col-line">Suite 210, PMB 4418</div>
      <div class="col-line">Seabrook, FL 34192</div>
    </div>

    <div class="footer-col col-contact">
      <div class="contact-block">
        <span class="marker sep-teal">+</span>
        <div class="col-title">Contact our support via e-mail</div>
        <div class="col-line">hello@elsiemarlowe.com</div>
      </div>
      <div class="contact-block">
        <span class="marker sep-lime">+</span>
        <div class="col-title">Call our office (555)218-0394</div>
      </div>
    </div>

    <div class="footer-brand">Elsie Marlowe</div>
  </footer>

</main>
</body>
</html>
```